Crumbly Corner needs a business card

Crumbly Corner needs an attractive, playful, and exciting business card design to attract potential buyers. I have included our logo, label, and social media design files along with the fonts and colors for ideas. For the logo file, please only pay attention to the purple background with white text. I want a card with premium matte and metallic finish. I want my name included, e-mail, and phone number. The logo must be included, and then use the label design and social media design files to add creativity to the design. Only the fonts that are provided should be used as well.

Name: Gregory Halvorsen
Phone: 555-274-8106
E-mail: ghalvorsen@crumblycornerco.example

Industry/Entity Type

Business

Contact Information for Business Card

I want a card with premium matte and metallic finish. I want my name included, e-mail, and phone number. The logo must be included, and then use the label design and social media design files to add creativity to the design. Only the fonts that are provided should be used as well.

Name: Gregory Halvorsen
Phone: 555-274-8106

Colors
6b449b

Requirements
Must have
• My logo, my fonts, my colors, my designs to some degree, and my character

```html
<!DOCTYPE html>
<html lang="en">
<head>
<meta charset="utf-8">
<title>Crumbly Corner – Business Card</title>
<link href="https://fonts.googleapis.com/css2?family=Questrial&display=swap" rel="stylesheet">
<style>
  :root {
    --purple: #35225f;
    --purple-line: #4a3580;
    --white: #ffffff;
    --ghost: #eeeef0;
    --ghost-deep: #e4e4e8;
    --backdrop: #2a2a2c;
  }
  * { margin: 0; padding: 0; box-sizing: border-box; }
  html, body {
    width: 1200px; height: 880px; overflow: hidden;
    background: var(--backdrop);
    font-family: "Questrial", "Century Gothic", sans-serif;
  }
  .sheet {
    width: 1200px; height: 880px;
    display: flex; align-items: center; justify-content: center; gap: 40px;
  }
  .card {
    position: relative;
    width: 560px; height: 320px;
    border-radius: 22px;
    overflow: hidden;
  }
  /* Back side */
  .card--back {
    background: var(--purple);
    display: flex; align-items: center; justify-content: center;
  }
  .brand {
    font-size: 34px;
    letter-spacing: 1px;
    white-space: nowrap;
  }
  .card--back .brand { color: var(--white); }

  /* Front side */
  .card--front { background: var(--white); }
  .watermark {
    position: absolute; left: 50px; top: 95px;
    width: 290px; height: 170px;
    border-radius: 120px 120px 10px 10px;
    background: radial-gradient(ellipse at 50% 40%, var(--ghost-deep), var(--ghost) 60%, rgba(238,238,240,0) 100%);
  }
  .card--front .brand {
    position: absolute; right: 40px; top: 62px;
    color: var(--purple);
  }
  .rule {
    position: absolute; height: 1px; background: var(--purple-line);
  }
  .rule--brand { right: 30px; top: 150px; width: 240px; }
  .rule--name { left: 36px; top: 228px; width: 250px; }
  .holder {
    position: absolute; left: 36px; top: 196px;
    color: var(--purple);
    font-size: 21px; font-weight: 700;
  }
  .contacts {
    position: absolute; left: 42px; top: 238px;
    list-style: none;
    color: var(--purple);
    font-size: 15px;
  }
  .contacts li { display: flex; align-items: center; gap: 8px; height: 20px; }
  .contacts svg { width: 14px; height: 14px; flex: none; }
  .band {
    position: absolute; left: 0; right: 0; bottom: 0;
    height: 34px; background: var(--purple);
  }
</style>
</head>
<body>
<main class="sheet">
  <section class="card card--back" aria-label="Card back">
    <span class="brand">Crumbly Corner</span>
  </section>

  <section class="card card--front" aria-label="Card front">
    <div class="watermark" role="img" aria-label="Faint brand decoration area"></div>
    <span class="brand">Crumbly Corner</span>
    <div class="rule rule--brand"></div>
    <p class="holder">Gregory Halvorsen</p>
    <div class="rule rule--name"></div>
    <ul class="contacts">
      <li>
        <svg viewBox="0 0 16 16" aria-hidden="true"><circle cx="8" cy="8" r="7" fill="none" stroke="var(--purple)" stroke-width="1.4"/><path d="M5.5 4.5l1.3 1.6-.7 1c.5 1 1.2 1.7 2.2 2.2l1-.7 1.6 1.3-.8 1.2c-2.8-.3-5.2-2.7-5.5-5.5z" fill="var(--purple)"/></svg>
        <span>555-274-8106</span>
      </li>
      <li>
        <svg viewBox="0 0 16 16" aria-hidden="true"><circle cx="8" cy="8" r="7.5" fill="var(--purple)"/><rect x="4" y="5" width="8" height="6" rx="0.8" fill="none" stroke="var(--white)" stroke-width="1"/><path d="M4 5.5l4 3 4-3" fill="none" stroke="var(--white)" stroke-width="1"/></svg>
        <span>ghalvorsen@crumblycornerco.example</span>
      </li>
    </ul>
    <div class="band"></div>
  </section>
</main>
</body>
</html>
```